Biz Card & Stationary: Modern, boutique appeal for vacation rental company for high end luxury homes
Biz Card + Folder + Letterhead + Envelope
Simple
Marla Whitcombe
Owner
2817 Maple Hollow Ln Austin TX 78529
marla@quolbi.com
www.quolbi.com
-may create image or graphic to use with logo -Need letterhead & envelopes in word format

```html
<!DOCTYPE html>
<html lang="en">
<head>
<meta charset="utf-8">
<title>Quolbi Business Card</title>
<link rel="stylesheet" href="https://fonts.googleapis.com/css2?family=Questrial&family=Open+Sans:wght@400;600&display=swap">
<style>
  :root {
    --backdrop: #d6d7d9;
    --card: #ffffff;
    --teal: #3bbdc8;
    --swoosh: #8a8b8d;
    --ink: #2f3b40;
    --brand: #3bb3bf;
  }
  * { margin: 0; padding: 0; box-sizing: border-box; }
  html, body { width: 1200px; height: 902px; overflow: hidden; }
  body {
    background: var(--backdrop);
    font-family: "Open Sans", Arial, sans-serif;
    display: flex;
    flex-direction: column;
    align-items: center;
    justify-content: center;
    gap: 34px;
  }
  .card {
    position: relative;
    width: 700px;
    height: 400px;
    background: var(--card);
    box-shadow: 0 6px 18px rgba(0,0,0,0.18);
    overflow: hidden;
  }
  .brand {
    font-family: "Questrial", Arial, sans-serif;
    color: var(--brand);
    font-weight: 400;
    letter-spacing: 1px;
    line-height: 1;
  }
  .card-front .brand {
    position: absolute;
    top: 50%; left: 50%;
    transform: translate(-50%, -50%);
    font-size: 78px;
  }
  .card-back .shape { position: absolute; inset: 0; }
  .card-back .brand {
    position: absolute;
    left: 58px;
    top: 262px;
    font-size: 64px;
  }
  .details {
    position: absolute;
    right: 44px;
    top: 44px;
    text-align: right;
    color: var(--ink);
    font-size: 15px;
    line-height: 1.45;
  }
  .details .name { font-weight: 600; font-size: 18px; }
  .details .role { margin-bottom: 22px; }
  .details .line { display: flex; justify-content: flex-end; align-items: center; gap: 8px; }
  .details .gap { margin-top: 18px; }
  .details svg { width: 13px; height: 13px; fill: var(--ink); }
</style>
</head>
<body>
  <section class="card card-front">
    <div class="brand">quolbi</div>
  </section>

  <section class="card card-back">
    <svg class="shape" viewBox="0 0 700 400" width="700" height="400" aria-hidden="true">
      <rect width="700" height="400" fill="var(--teal)"/>
      <path d="M0,130 C230,110 400,210 420,400 L0,400 Z" fill="var(--card)"/>
      <path d="M430,220 C470,270 490,330 488,400 L452,400 C452,330 445,270 430,220 Z" fill="var(--swoosh)"/>
    </svg>
    <div class="brand">quolbi</div>
    <div class="details">
      <div class="name">Marla Whitcombe</div>
      <div class="role">Owner</div>
      <div class="line">2817 Maple Hollow Ln,</div>
      <div class="line">Austin TX 78529</div>
      <div class="line">512 555 0148
        <svg viewBox="0 0 24 24"><path d="M6.6 10.8a15 15 0 0 0 6.6 6.6l2.2-2.2a1 1 0 0 1 1-.25 11 11 0 0 0 3.6.6 1 1 0 0 1 1 1V20a1 1 0 0 1-1 1A17 17 0 0 1 3 4a1 1 0 0 1 1-1h3.5a1 1 0 0 1 1 1 11 11 0 0 0 .6 3.6 1 1 0 0 1-.25 1z"/></svg>
      </div>
      <div class="line">512 555 0149
        <svg viewBox="0 0 24 24"><path d="M6 3h10v5H6zM4 9h16a2 2 0 0 1 2 2v6h-4v4H6v-4H2v-6a2 2 0 0 1 2-2zm4 8v2h8v-2z"/></svg>
      </div>
      <div class="line gap">marla@quolbi.com</div>
      <div class="line">www.quolbi.com</div>
    </div>
  </section>
</body>
</html>
```